Welcome Card

We are a property management company and I need to attach this postcard to 2 packages of microwave popcorn as a welcome gift to our new tenant.Here is the copy for the postcard (FRONT SIDE): Just "popped" in to make sure your apartment was ready for you! Enjoy your Stay.........UNITED APARTMENTSBACK SIDE: Welcome image with the words "Thank You"

Industry/Entity Type

It Company

Font styles to use
Sans Serif

```html
<!DOCTYPE html>
<html lang="en">
<head>
<meta charset="utf-8">
<title>Bramble Apartments – Welcome Postcard</title>
<link rel="stylesheet" href="https://fonts.googleapis.com/css2?family=Alegreya:wght@400;500&family=Great+Vibes&family=Playfair+Display:wght@900&display=swap">
<style>
  :root {
    --backdrop: #1f1f1f;
    --card-white: #ffffff;
    --popcorn-light: #f4ead2;
    --popcorn-mid: #e2cfa2;
    --popcorn-deep: #c9ad74;
    --stripe-red: #e2231a;
    --ink-black: #1a1a1a;
    --frame-grey: #6e6e6e;
    --script-grey: #777777;
    --brand-blue: #1d4f9c;
  }
  * { box-sizing: border-box; margin: 0; padding: 0; }
  html, body {
    width: 800px;
    height: 1200px;
    overflow: hidden;
    background: var(--backdrop);
  }
  .canvas {
    position: relative;
    width: 800px;
    height: 1200px;
  }
  .card {
    position: absolute;
    left: 60px;
    width: 680px;
    overflow: hidden;
    background: var(--card-white);
  }
  .card svg { position: absolute; inset: 0; }

  /* Front side */
  .card--front { top: 40px; height: 540px; }
  .front-message {
    position: absolute;
    left: 0;
    right: 0;
    top: 300px;
    text-align: center;
    font-family: "Alegreya", Georgia, serif;
  }
  .brand-name {
    position: absolute;
    left: 0;
    right: 0;
    top: 236px;
    text-align: center;
    font-family: "Alegreya", Georgia, serif;
    font-weight: 500;
    font-size: 34px;
    letter-spacing: 1px;
    color: var(--brand-blue);
  }
  .front-message__lead {
    font-size: 23px;
    line-height: 1.3;
    color: var(--ink-black);
  }
  .front-message__signoff {
    margin-top: 4px;
    font-size: 25px;
    line-height: 1.15;
    color: var(--stripe-red);
  }

  /* Back side */
  .card--back { top: 620px; height: 540px; }
  .back-words {
    position: absolute;
    left: 0;
    right: 0;
    text-align: center;
  }
  .back-words__welcome {
    top: 92px;
    font-family: "Great Vibes", cursive;
    font-size: 112px;
    line-height: 1;
    color: var(--script-grey);
  }
  .back-words__thanks {
    top: 222px;
    font-family: "Playfair Display", Georgia, serif;
    font-weight: 900;
    font-size: 118px;
    line-height: 1.02;
    color: var(--stripe-red);
  }
</style>
</head>
<body>
<main class="canvas">

  <section class="card card--front" aria-label="Postcard front">
    <svg width="680" height="540" viewBox="0 0 680 540">
      <defs>
        <linearGradient id="popcorn-field" x1="0" y1="0" x2="1" y2="1">
          <stop offset="0" stop-color="var(--popcorn-light)"/>
          <stop offset="0.5" stop-color="var(--popcorn-mid)"/>
          <stop offset="1" stop-color="var(--popcorn-deep)"/>
        </linearGradient>
        <linearGradient id="popcorn-box" x1="0" y1="0" x2="0" y2="1">
          <stop offset="0" stop-color="#f3d9c4"/>
          <stop offset="1" stop-color="#f0c3bd"/>
        </linearGradient>
      </defs>
      <rect class="popcorn-photo" width="680" height="540" fill="url(#popcorn-field)" role="img" aria-label="Photo of a heap of popped popcorn"/>
      <polygon class="popcorn-box" points="40,170 640,170 615,540 65,540" fill="url(#popcorn-box)" role="img" aria-label="Illustrated red and white striped popcorn box overflowing with popcorn, with two cartoon kids peeking out"/>
      <ellipse class="message-oval" cx="340" cy="345" rx="268" ry="168" fill="var(--card-white)" stroke="var(--stripe-red)" stroke-width="5"/>
    </svg>
    <p class="brand-name">BRAMBLE APARTMENTS</p>
    <div class="front-message">
      <p class="front-message__lead">Just "popped" in to make sure<br>your apartment was ready for you!</p>
      <p class="front-message__signoff">Enjoy<br>your Stay</p>
    </div>
  </section>

  <section class="card card--back" aria-label="Postcard back">
    <svg width="680" height="540" viewBox="0 0 680 540">
      <rect class="stripe-field" width="680" height="540" fill="var(--stripe-red)" role="img" aria-label="Diagonal red and white candy stripe pattern"/>
      <path class="name-plaque" d="M120,40 H560 A40,40 0 0 0 600,80 V460 A40,40 0 0 0 560,500 H120 A40,40 0 0 0 80,460 V80 A40,40 0 0 0 120,40 Z"
            fill="var(--card-white)" stroke="var(--frame-grey)" stroke-width="14"/>
      <path class="name-plaque__inner" d="M126,56 H554 A36,36 0 0 0 584,86 V454 A36,36 0 0 0 554,484 H126 A36,36 0 0 0 96,454 V86 A36,36 0 0 0 126,56 Z"
            fill="none" stroke="var(--frame-grey)" stroke-width="2"/>
    </svg>
    <p class="back-words back-words__welcome">Welcome</p>
    <p class="back-words back-words__thanks">Thank<br>You</p>
  </section>

</main>
</body>
</html>
```